Zarqa Fowl "The Tender Path"

I need a business card design and a logo design for my business. It's a delivery business of halal poultry (chicken). I would the business card to include the following information.
-business name: Zarqa Fowl
-business tag line: "The Tender Path"
Name: Tariq Moussef
Contact number: 07812450937
E-mail: zarqa_fowl@mailbox-example.com
Website: www.zarqafowl-example.com
Also need a business logo also included relating to the business.
I would like it professional yet creative. Something original. I want it to have 2 main colours included.
I want it to have a middle Eastern/ Arabic look if possible.
Thanks :)
Target Market(s)
Butchers
Restaurants
Industry/Entity Type
Business
Contact Information for Business Card
Business name: Zarqa fowl
Business tag line: "The Tender Path"
E-mail: zarqa_fowl@mailbox-example.com
Name: Tariq Moussef

```html
<!DOCTYPE html>
<html lang="en">
<head>
<meta charset="utf-8">
<title>Zarqa Fowl – Business Card</title>
<link rel="stylesheet" href="https://fonts.googleapis.com/css2?family=Tinos:ital,wght@0,400;0,700;1,400&display=swap">
<style>
  :root {
    --brand-red: #d2060b;
    --brand-red-light: #e4454a;
    --paper: #ffffff;
    --ink: #1c1c1c;
    --backdrop: #e9e6e2;
    --watermark: rgba(210, 6, 11, 0.08);
  }
  * { box-sizing: border-box; margin: 0; padding: 0; }
  html, body {
    width: 1200px;
    height: 900px;
    overflow: hidden;
    background: var(--backdrop);
    font-family: "Tinos", "Times New Roman", serif;
  }
  .card-set {
    position: relative;
    width: 1200px;
    height: 900px;
  }
  .card {
    position: absolute;
    top: 300px;
    width: 525px;
    height: 300px;
    box-shadow: 0 6px 18px rgba(0, 0, 0, 0.18);
    overflow: hidden;
  }

  /* Contact side */
  .card--contact {
    left: 50px;
    background: var(--paper);
    color: var(--ink);
  }
  .card--contact .brand {
    position: absolute;
    top: 22px;
    left: 26px;
    display: flex;
    align-items: center;
    gap: 12px;
  }
  .brand-dot {
    width: 44px;
    height: 44px;
    border: 3px solid var(--brand-red);
    border-radius: 50%;
  }
  .brand-name {
    font-size: 22px;
    font-weight: 400;
    color: var(--brand-red);
    letter-spacing: 1px;
    text-transform: uppercase;
  }
  .brand-tagline {
    position: absolute;
    top: 64px;
    left: 200px;
    font-size: 11px;
    font-style: italic;
    color: var(--ink);
  }
  .holder-name {
    position: absolute;
    top: 92px;
    left: 28px;
    font-size: 19px;
  }
  .watermark {
    position: absolute;
    right: 40px;
    bottom: 26px;
    width: 170px;
    height: 170px;
    border-radius: 50%;
    background: var(--watermark);
  }
  .contact-list {
    position: absolute;
    right: 26px;
    bottom: 24px;
    list-style: none;
    text-align: right;
    font-size: 12px;
    line-height: 1.55;
  }

  /* Brand side */
  .card--brand {
    left: 625px;
    background: linear-gradient(135deg, var(--brand-red-light) 0%, var(--brand-red) 45%, var(--brand-red) 100%);
    color: var(--paper);
    display: flex;
    flex-direction: column;
    align-items: center;
    justify-content: center;
  }
  .card--brand .brand-dot {
    width: 110px;
    height: 110px;
    border: 4px solid var(--paper);
    margin-bottom: 12px;
  }
  .card--brand .brand-name {
    color: var(--paper);
    font-size: 27px;
  }
  .card--brand .brand-tagline {
    position: static;
    align-self: flex-end;
    margin-right: 140px;
    color: var(--paper);
    font-size: 13px;
  }
</style>
</head>
<body>
  <main class="card-set">
    <section class="card card--contact" aria-label="Business card, contact side">
      <div class="brand">
        <span class="brand-dot"></span>
        <span class="brand-name">Zarqa Fowl</span>
      </div>
      <p class="brand-tagline">The Tender Path</p>
      <p class="holder-name">Tariq Moussef</p>
      <div class="watermark" aria-hidden="true"></div>
      <ul class="contact-list">
        <li>Suite 4, 123 Market Road</li>
        <li>Tel: 07812450937</li>
        <li>Email: zarqa_fowl@mailbox-example.com</li>
        <li>www.zarqafowl-example.com</li>
      </ul>
    </section>

    <section class="card card--brand" aria-label="Business card, brand side">
      <span class="brand-dot"></span>
      <span class="brand-name">Zarqa Fowl</span>
      <p class="brand-tagline">The Tender Path</p>
    </section>
  </main>
</body>
</html>
```